Labels for new organic cosmetics/personal care brand called Noveri

I need labels for new cosmetic brand named ( Noveri )
It is natural and organic
products include:
**natural soaps 3 in a box ( 7 types): shea butter soap, almond soap, lavender soap, apricot soap, olive soap , camel milk soap and sensitive skin soap.

**Organic shea butters (7 types) (in round container) pure shea butter, Shea butter with argan oil, shea butter with olive oil, shea butter with oats, Shea butter with camel milk, shea butter with camel milk and Agarwood and shea butter with donky milk.

**deodorant: one type only , a crystal deodorant.

**shampoo (in cylindrical container) : one type natural shampoo

** Organic Oils (two types) (in clyndrical container) : Argan oil and Rose hip oil.

attached examples of similar containers and outline of labels that i want to have new ones.
**notice:
shape of shea butter container is round and flat.
shape of shampoo is cylindrical.
shape of soaps is a cuboid box.

Target Market(s)

men and women of all ages

Industry/Entity Type

Cosmetics

Font styles to use
Sans Serif

Colors
e4daeb
f9d9e8
fbd4d5
fee3d5
fce8d3
fff3d1
fdf9cf
cee9f5
cadf82

Requirements
Must have
• * Noveri logo
• * organic/natural theme
• * front and back labels
• * 7 labels for soaps, 7 back and 7 front labels for shea butter, one label for deoderant, one label for shampoo, two labels for natural oils.
Nice to have
• leaves, green colors or natural shades of colors , pastel colors
• the color is not specified
Should not have
• **I don't need the container design** .
• just the labels. attached are outline example of the labels and photos of the products so you know the shape of container.
• shape of shea butter container is round and flat.
• shape of shampoo is cylindrical.
• shape of soaps is a cuboid box.

```html
<!DOCTYPE html>
<html lang="fr">
<head>
<meta charset="utf-8">
<title>Noveri – Shampooing naturel Abricot</title>
<link rel="stylesheet" href="https://fonts.googleapis.com/css2?family=Arimo:wght@400;700&family=Tinos:wght@700&display=swap">
<style>
  :root {
    --page: #ffffff;
    --label-edge: #fde6cf;
    --label-body: #f9d6b2;
    --label-glow: #fde3cb;
    --frame-line: #f3ad72;
    --column-light: #f6b87f;
    --column-deep: #f2a562;
    --accent-text: #e5893a;
    --band: #f2a462;
    --badge-fill: #fbc99a;
    --ink-light: #ffffff;
  }
  html, body {
    margin: 0;
    padding: 0;
    width: 1200px;
    height: 4507px;
    overflow: hidden;
    background: var(--page);
  }
  .shampoo-label {
    display: block;
    width: 1200px;
    height: 4507px;
  }
  .label-edge { fill: var(--label-edge); }
  .label-body { fill: url(#bodyGlow); stroke: var(--frame-line); stroke-width: 1.6; }
  .column-light { fill: var(--column-light); }
  .column-deep { fill: var(--column-deep); }
  .brand-name {
    font-family: "Arimo", Arial, sans-serif;
    font-weight: 400;
    font-size: 64px;
    fill: var(--ink-light);
  }
  .brand-dot { fill: var(--ink-light); }
  .product-type-fr {
    font-family: "Arimo", Arial, sans-serif;
    font-weight: 400;
    font-size: 44px;
    fill: var(--ink-light);
  }
  .product-scent-fr {
    font-family: "Arimo", Arial, sans-serif;
    font-weight: 700;
    font-size: 112px;
    fill: var(--ink-light);
  }
  .product-name-en {
    font-family: "Arimo", Arial, sans-serif;
    font-weight: 400;
    font-size: 40px;
    fill: var(--accent-text);
  }
  .product-name-en tspan.scent { font-weight: 700; }
  .organic-badge { fill: var(--badge-fill); }
  .origin-band { fill: var(--band); }
  .origin-title {
    font-family: "Tinos", "Times New Roman", serif;
    font-weight: 700;
    font-size: 15px;
    fill: var(--ink-light);
  }
  .origin-note {
    font-family: "Tinos", "Times New Roman", serif;
    font-weight: 700;
    font-size: 6px;
    fill: var(--ink-light);
  }
  .net-rule { stroke: var(--ink-light); stroke-width: 1.6; }
  .net-label, .net-weight {
    font-family: "Arimo", Arial, sans-serif;
    fill: var(--ink-light);
  }
  .net-label { font-size: 15px; }
  .net-weight { font-size: 16px; font-weight: 700; }
</style>
</head>
<body>
<svg class="shampoo-label" viewBox="0 0 400 1502.3" xmlns="http://www.w3.org/2000/svg" role="img" aria-label="Noveri natural apricot shampoo label">
  <defs>
    <linearGradient id="bodyGlow" x1="1" y1="0" x2="0" y2="1">
      <stop offset="0" stop-color="var(--label-glow)"/>
      <stop offset="0.55" stop-color="var(--label-body)"/>
      <stop offset="1" stop-color="var(--label-body)"/>
    </linearGradient>
  </defs>

  <!-- outer label shape -->
  <path class="label-edge" d="M0,1502.3 V200 A200,200 0 0 1 400,200 V1502.3 Z"/>
  <!-- inner framed panel with soft tone where the leaf sweeps sit -->
  <path class="label-body" role="img" aria-label="Soft pale leaf sweeps across the background" d="M20,1475 V200 A180,180 0 0 1 380,200 V1475 Z"/>

  <!-- brand -->
  <g class="brand">
    <circle class="brand-dot" cx="106" cy="246" r="9"/>
    <text class="brand-name" x="210" y="270" text-anchor="middle">Noveri</text>
  </g>

  <!-- colour columns -->
  <path class="column-light" d="M20,1275 V452 H95 A140,158 0 0 1 235,610 V1275 Z"/>
  <path class="column-deep" d="M92,1275 V452 H95 A140,158 0 0 1 235,610 V1275 Z"/>

  <!-- product names -->
  <text class="product-type-fr" transform="translate(74,1122) rotate(-90)" textLength="420" lengthAdjust="spacingAndGlyphs">Shampooing naturel</text>
  <text class="product-scent-fr" transform="translate(205,1130) rotate(-90)" textLength="366" lengthAdjust="spacingAndGlyphs">ABRICOT</text>
  <text class="product-name-en" transform="translate(289,1130) rotate(-90)" textLength="430" lengthAdjust="spacingAndGlyphs">Natural Shampoo <tspan class="scent">APRICOT</tspan></text>

  <!-- certification badge -->
  <circle class="organic-badge" cx="318" cy="1216" r="40"/>

  <!-- origin band -->
  <rect class="origin-band" x="20" y="1286" width="360" height="50"/>
  <text class="origin-title" x="200" y="1313" text-anchor="middle">FABRIQUÉ EN FRANCE</text>
  <text class="origin-note" x="200" y="1325" text-anchor="middle">TESTÉ SOUS  CONTRÔLE DERMATOLOGIQUE</text>

  <!-- net weight -->
  <line class="net-rule" x1="80" y1="1390" x2="155" y2="1390"/>
  <line class="net-rule" x1="245" y1="1390" x2="320" y2="1390"/>
  <text class="net-label" x="200" y="1395" text-anchor="middle">Net Wt</text>
  <text class="net-weight" x="200" y="1424" text-anchor="middle">75 gr  •  2.65 oz</text>
</svg>
</body>
</html>
```